Valbrook Data Works

Our company is about IT hardwares and IT solutions. IT hardware such as PC, RAMS, storage and servers. IT solutions such as project management, BA. We are also selling new technology too.

Target Market(s)

Consumer, Small to Medium Business, Corporate

Requirements
Must have
• The business card must have the following:
• Name:
• Title:
• Contact Number:
• Email address:
• Website:
• Color: Must match the logo color upgrade

```html
<!DOCTYPE html>
<html lang="en">
<head>
<meta charset="utf-8">
<title>Valbrook Data Works – Business Card</title>
<link rel="stylesheet" href="https://fonts.googleapis.com/css2?family=Open+Sans:wght@400;700&display=swap">
<style>
  :root {
    --page: #ffffff;
    --card-grey: #b4b0b1;
    --orange-deep: #c96a2f;
    --orange-light: #d98e37;
    --brand-orange: #d5792c;
    --ink: #4a3f3c;
    --white: #ffffff;
  }
  * { margin: 0; padding: 0; box-sizing: border-box; }
  html, body {
    width: 1200px; height: 1200px; overflow: hidden;
    background: var(--page);
    font-family: "Open Sans", sans-serif;
  }
  .canvas { position: relative; width: 1200px; height: 1200px; }
  .card {
    position: absolute; left: 246px; width: 730px; height: 438px;
    background: var(--card-grey); overflow: hidden;
  }
  .card--front { top: 160px; }
  .card--back { top: 666px; }

  .brand { position: absolute; display: flex; flex-direction: column; align-items: center; }
  .brand__dot { border-radius: 50%; background: var(--brand-orange); }
  .brand__name {
    font-family: "Open Sans", sans-serif; font-weight: 700; color: var(--white);
    text-align: center; letter-spacing: 1px; line-height: 1.1;
  }
  .card--front .brand { left: 0; right: 0; top: 110px; }
  .card--front .brand__dot { width: 74px; height: 74px; margin-bottom: 34px; }
  .card--front .brand__name { font-size: 44px; }
  .card--back .brand { left: 0; width: 365px; top: 84px; }
  .card--back .brand__dot { width: 46px; height: 46px; margin-bottom: 22px; }
  .card--back .brand__name { font-size: 27px; }

  .info-panel {
    position: absolute; left: 365px; top: 0; width: 365px; height: 438px;
    background: linear-gradient(110deg, var(--orange-deep), var(--orange-light));
  }
  .tab {
    position: absolute; left: 352px; top: 200px; width: 26px; height: 170px;
    border-radius: 6px; background: linear-gradient(180deg, var(--orange-light), var(--orange-deep));
  }
  .tab::after {
    content: ""; position: absolute; left: 9px; top: 4px; width: 13px; height: 162px;
    background: var(--card-grey); border-radius: 2px;
  }
  .holder {
    position: absolute; left: 408px; top: 72px; color: var(--white);
  }
  .holder__name { font-size: 29px; font-weight: 400; line-height: 36px; }
  .holder__title { font-size: 15px; font-weight: 400; line-height: 20px; margin-top: 4px; letter-spacing: 0.5px; }
  .contact-list { position: absolute; left: 408px; top: 202px; list-style: none; }
  .contact-item { position: relative; display: flex; align-items: center; color: var(--white); font-size: 14px; line-height: 18px; }
  .contact-item svg { width: 34px; height: 34px; flex: none; margin-right: 11px; fill: var(--ink); }
  .contact-item--address { height: 44px; }
  .contact-item--phone { height: 40px; }
  .contact-item--email { height: 38px; margin-top: 12px; }
  .contact-item--web { height: 38px; margin-top: 10px; }
</style>
</head>
<body>
<main class="canvas">
  <section class="card card--front">
    <div class="brand">
      <span class="brand__dot"></span>
      <span class="brand__name">VALBROOK<br>DATA WORKS</span>
    </div>
  </section>

  <section class="card card--back">
    <div class="brand">
      <span class="brand__dot"></span>
      <span class="brand__name">VALBROOK<br>DATA WORKS</span>
    </div>
    <div class="info-panel"></div>
    <div class="tab"></div>
    <div class="holder">
      <h1 class="holder__name">Rowan Hale</h1>
      <p class="holder__title">Sales Manager</p>
    </div>
    <ul class="contact-list">
      <li class="contact-item contact-item--address">
        <svg viewBox="0 0 34 34" aria-hidden="true"><path d="M17 3a9 9 0 0 0-9 9c0 7 9 19 9 19s9-12 9-19a9 9 0 0 0-9-9zm0 12.5a3.5 3.5 0 1 1 0-7 3.5 3.5 0 0 1 0 7z"/></svg>
        <span>PO Box 000000<br>Address</span>
      </li>
      <li class="contact-item contact-item--phone">
        <svg viewBox="0 0 34 34" aria-hidden="true"><circle cx="17" cy="17" r="15" fill="none" stroke="#4a3f3c" stroke-width="2.5"/><path d="M12 9c1-.6 2-.3 2.5.6l1.4 2.7c.4.8.2 1.6-.5 2.1l-1 .7c.8 2 2.3 3.6 4.2 4.6l.8-1c.5-.6 1.4-.8 2.1-.4l2.6 1.5c.8.5 1 1.5.5 2.4-1 1.8-3 2.5-5 1.7-4.2-1.8-7.3-5.2-8.6-9.5-.5-2 .2-3.7 1-4.4z"/></svg>
        <span>000 000 000</span>
      </li>
      <li class="contact-item contact-item--email">
        <svg viewBox="0 0 34 34" aria-hidden="true"><path d="M2 7h30v20H2z M4 9v1l13 9 13-9V9z M4 12.5V25h26V12.5l-13 9z" fill-rule="evenodd"/></svg>
        <span>rowan@valbrookdataworks.com</span>
      </li>
      <li class="contact-item contact-item--web">
        <svg viewBox="0 0 34 34" aria-hidden="true"><circle cx="17" cy="17" r="15" fill="none" stroke="#4a3f3c" stroke-width="2.5"/><path d="M2 17h30M17 2c-5 5-5 25 0 30M17 2c5 5 5 25 0 30M5 9h24M5 25h24" fill="none" stroke="#4a3f3c" stroke-width="1.5"/><rect x="1" y="13" width="32" height="8" fill="#d17f33"/><text x="17" y="19.5" font-size="7" font-family="Open Sans, sans-serif" font-weight="700" text-anchor="middle" fill="#4a3f3c">www</text></svg>
        <span>www.valbrookdataworks.com</span>
      </li>
    </ul>
  </section>
</main>
</body>
</html>
```